Redesign of existing business card

I would like the "signage" attachment converted into a business card. This needs to be double sided aswell, keeping the phone number and names on the front, and the email + website on the back.

Second attachment is the current business card design.

Larger font for contact details is required.

Must keep to original color themes (electric blue, silver/grey etc)

Back of the card to have blue background with white writing.

Industry/Entity Type

Business

Contact Information for Business Card

Refer to existing design from attachments

Requirements
Must have
• Refer to existing design from attachments
Nice to have

```html
<!DOCTYPE html>
<html lang="en">
<head>
<meta charset="UTF-8">
<title>Voltara Power Services — Business Card</title>
<link href="https://fonts.googleapis.com/css2?family=Roboto:wght@300;400;700&display=swap" rel="stylesheet">
<style>
  :root {
    --electric-blue: #1f1ee6;
    --silver: #8f9298;
    --ink-grey: #6d7077;
    --card-white: #ffffff;
    --backdrop: #2b2b2e;
  }
  * { margin: 0; padding: 0; box-sizing: border-box; }
  html, body {
    width: 1200px; height: 950px; overflow: hidden;
    background: var(--backdrop);
    font-family: "Roboto", Arial, sans-serif;
  }
  .sheet {
    width: 1200px; height: 950px;
    display: flex; flex-direction: column;
    align-items: center; justify-content: center; gap: 40px;
  }
  .card {
    position: relative;
    width: 740px; height: 423px;
    overflow: hidden;
  }
  .card--front { background: var(--card-white); }
  .card--front .edge-band {
    position: absolute; left: 0; right: 0; bottom: 0; height: 12px;
    background: var(--electric-blue);
  }
  .brand {
    position: absolute;
    display: flex; align-items: center; gap: 14px;
  }
  .brand__dot {
    width: 46px; height: 46px; border-radius: 50%;
    flex: none;
  }
  .brand__name {
    font-weight: 700; font-size: 40px; letter-spacing: 1px; line-height: 1;
    text-transform: uppercase;
  }
  .card--front .brand { left: 230px; top: 118px; }
  .card--front .brand__dot { background: var(--silver); }
  .card--front .brand__name { color: var(--electric-blue); }

  .person {
    position: absolute; left: 56px; bottom: 108px;
  }
  .person__name {
    color: var(--electric-blue); font-weight: 700; font-size: 22px;
    text-transform: uppercase; letter-spacing: 0.5px;
  }
  .person__role {
    color: var(--ink-grey); font-weight: 300; font-size: 17px; margin-top: 4px;
  }
  .contacts {
    position: absolute; left: 56px; bottom: 36px;
    list-style: none; display: flex; gap: 30px;
  }
  .contacts li {
    display: flex; align-items: center; gap: 8px;
    color: var(--ink-grey); font-size: 16px;
  }
  .contacts svg { width: 18px; height: 18px; flex: none; }

  .card--back { background: var(--electric-blue); }
  .card--back .brand { left: 0; right: 0; top: 0; bottom: 0; justify-content: center; }
  .card--back .brand__dot { background: var(--card-white); width: 54px; height: 54px; }
  .card--back .brand__name { color: var(--card-white); font-size: 46px; }
  .card--back .web {
    position: absolute; left: 44px; bottom: 34px;
    color: var(--card-white); font-weight: 300; font-size: 15px; letter-spacing: 4px;
  }
</style>
</head>
<body>
<main class="sheet">
  <section class="card card--front" aria-label="Card front">
    <div class="brand">
      <span class="brand__dot"></span>
      <span class="brand__name">Voltara Power Services</span>
    </div>
    <div class="person">
      <p class="person__name">Liam Carter</p>
      <p class="person__role">President</p>
    </div>
    <ul class="contacts">
      <li>
        <svg viewBox="0 0 18 18"><circle cx="9" cy="9" r="9" fill="#1f1ee6"/><path d="M6 5.2l1.6-.4.9 2.2-1 .8a6 6 0 0 0 2.7 2.7l.8-1 2.2.9-.4 1.6c-3.8.3-7.1-3-6.8-6.8z" fill="#fff"/></svg>
        <span>555 0142 7781</span>
      </li>
      <li>
        <svg viewBox="0 0 18 18"><circle cx="9" cy="9" r="9" fill="#1f1ee6"/><rect x="4.5" y="6" width="9" height="6.5" rx="0.8" fill="#fff"/><path d="M4.8 6.4L9 9.6l4.2-3.2" stroke="#1f1ee6" stroke-width="1" fill="none"/></svg>
        <span>liam@voltarapower.com</span>
      </li>
      <li>
        <svg viewBox="0 0 18 18"><circle cx="9" cy="9" r="9" fill="#1f1ee6"/><circle cx="9" cy="9" r="4.5" stroke="#fff" stroke-width="1.1" fill="none"/><path d="M4.5 9h9M9 4.5c-2 2.6-2 6.4 0 9M9 4.5c2 2.6 2 6.4 0 9" stroke="#fff" stroke-width="0.9" fill="none"/></svg>
        <span>www.voltarapower.com</span>
      </li>
    </ul>
    <div class="edge-band"></div>
  </section>

  <section class="card card--back" aria-label="Card back">
    <div class="brand">
      <span class="brand__dot"></span>
      <span class="brand__name">Voltara Power Services</span>
    </div>
    <p class="web">www.voltarapower.com.au</p>
  </section>
</main>
</body>
</html>
```